Cool Simple Design for Baby Product

Our company is Tovarin. We need a package design for our cupboard lock product. We want to appear as caring, warm and close to earth company that aims to improve family life.

Logo is our company logo, colour can be changed if you feel the need for it. Pics 1 and 2 are of the product itself. Pics 3 to 6 are examples of packages and visuals that I do like very much, maybe something along those lines.

Pics 7 and 8 a re just examples of something that I do NOT like. They feel too busy and detailed.

UPDATE: Colourbox1 is the main file that you should work on, colourbox2 is sample of the suppliers default look, so you can see how it looks when it is assembled.

There will be little text, but not much, ALSO there will be text in Germany so please consider this when creating the design. It is not yet finalized what text there will be but something like this:

"Text1: This is English text and there will not be much more than these characters, but also there will be German translation in this same space"

"Text2: Maybe this text too, overall 300 English characters maximum on whole package and that's it"

Industry/Entity Type

Baby

Font styles to use
Decorative
Script

Requirements
Must have
• Simple, soothing, cool, valuable.
Nice to have
• Less is more.
Should not have
• Aggressive with lot of details and too much stuff.

```html
<!DOCTYPE html>
<html lang="en">
<head>
<meta charset="utf-8">
<title>Tovarin cupboard lock mailer box dieline</title>
<link rel="stylesheet" href="https://fonts.googleapis.com/css2?family=Arimo&family=Great+Vibes&display=swap">
<style>
  :root {
    --paper: #ffffff;
    --panel: #fbf8d6;
    --band: #a3d4aa;
    --band-dark: #8cc895;
    --fold: #6fbf6f;
    --cut: #a0509a;
    --measure: #9b4f96;
    --brand: #5e9e68;
    --ring: #9fd3a6;
    --note: #f4fbf2;
    --ink: #222222;
  }
  html, body {
    margin: 0;
    padding: 0;
    width: 1200px;
    height: 1200px;
    overflow: hidden;
    background: var(--paper);
  }
  .dieline { display: block; width: 1200px; height: 1200px; }
  .measure-line { stroke: var(--measure); stroke-width: 1.3; fill: none; }
  .measure-label { font-family: "Arimo", Arial, sans-serif; font-size: 24px; fill: var(--ink); }
  .panel { fill: var(--panel); stroke: var(--cut); stroke-width: 1.2; }
  .fold { stroke: var(--fold); stroke-width: 1.1; stroke-dasharray: 9 6; fill: none; }
  .band { fill: var(--band); }
  .band-stitch { stroke: #ffffff; stroke-width: 1.5; stroke-dasharray: 7 5; fill: none; }
  .slot { fill: #ffffff; stroke: var(--cut); stroke-width: 1.2; }
  .name-disc { fill: #ffffff; }
  .brand-name { font-family: "Arimo", Arial, sans-serif; font-size: 20px; fill: var(--brand); }
  .hero-ring { fill: #ffffff; stroke: var(--ring); stroke-width: 14; }
  .info-panel { fill: var(--band-dark); }
  .info-text { font-family: "Great Vibes", cursive; font-size: 14px; fill: var(--note); }
</style>
</head>
<body>
<svg class="dieline" viewBox="0 0 1500 1500" xmlns="http://www.w3.org/2000/svg">
  <defs>
    <clipPath id="top-flap-clip">
      <path d="M557 200 L1120 200 L1122 208 C1200 215 1245 250 1245 290 C1245 320 1235 335 1225 337 L1105 348 L1105 358 L572 358 L572 348 L452 337 C440 335 432 320 432 290 C432 250 477 215 555 208 Z"/>
    </clipPath>
    <clipPath id="front-clip">
      <path d="M557 742 L1127 742 L1127 755 L1255 755 Q1265 755 1265 765 L1265 875 Q1265 885 1255 885 L1127 885 L1127 895 L557 895 L557 885 L424 885 Q414 885 414 875 L414 765 Q414 755 424 755 L557 755 Z"/>
    </clipPath>
    <radialGradient id="hero-fill" cx="50%" cy="50%" r="50%">
      <stop offset="0%" stop-color="#eef0b8"/>
      <stop offset="100%" stop-color="#d6ebdc"/>
    </radialGradient>
  </defs>

  <g class="measurements">
    <line class="measure-line" x1="216" y1="68" x2="216" y2="240"/>
    <line class="measure-line" x1="1457" y1="65" x2="1457" y2="237"/>
    <line class="measure-line" x1="216" y1="134" x2="1457" y2="132"/>
    <path class="measure-line" d="M228 128 L216 134 L228 140 M1445 126 L1457 132 L1445 138"/>
    <text class="measure-label" x="848" y="118" text-anchor="middle">325 mm</text>

    <line class="measure-line" x1="50" y1="201" x2="327" y2="201"/>
    <line class="measure-line" x1="53" y1="1427" x2="330" y2="1427"/>
    <line class="measure-line" x1="150" y1="203" x2="150" y2="1427"/>
    <path class="measure-line" d="M144 215 L150 203 L156 215 M144 1415 L150 1427 L156 1415"/>
    <text class="measure-label" x="80" y="858" text-anchor="middle">321 mm</text>
  </g>

  <g class="top-flap">
    <path class="panel" d="M557 200 L1120 200 L1122 208 C1200 215 1245 250 1245 290 C1245 320 1235 335 1225 337 L1105 348 L1105 358 L572 358 L572 348 L452 337 C440 335 432 320 432 290 C432 250 477 215 555 208 Z"/>
    <g clip-path="url(#top-flap-clip)">
      <rect class="band" x="420" y="248" width="840" height="62"/>
      <line class="band-stitch" x1="420" y1="259" x2="1260" y2="259"/>
      <line class="band-stitch" x1="420" y1="299" x2="1260" y2="299"/>
    </g>
    <line class="fold" x1="557" y1="200" x2="557" y2="350"/>
    <line class="fold" x1="1120" y1="200" x2="1120" y2="350"/>
    <circle class="name-disc" cx="847" cy="278" r="48"/>
    <text class="brand-name" x="847" y="285" text-anchor="middle" transform="rotate(180 847 278)">Tovarin</text>
  </g>

  <g class="lid">
    <path class="panel" d="M572 358 L440 408 Q432 415 432 430 L432 660 Q432 680 442 690 L560 742 L572 742 Z"/>
    <path class="panel" d="M1105 358 L1237 408 Q1245 415 1245 430 L1245 660 Q1245 680 1235 690 L1117 742 L1105 742 Z"/>
    <rect class="panel" x="572" y="358" width="533" height="384"/>
    <line class="fold" x1="572" y1="358" x2="1105" y2="358"/>
    <line class="fold" x1="572" y1="742" x2="1105" y2="742"/>
    <line class="fold" x1="572" y1="358" x2="572" y2="742"/>
    <line class="fold" x1="1105" y1="358" x2="1105" y2="742"/>
    <circle class="hero-ring" cx="845" cy="550" r="116"/>
    <circle cx="845" cy="550" r="100" fill="url(#hero-fill)" role="img" aria-label="Illustration of a baby reaching for a locked cupboard door, with the hand-lettered word Locked"/>
  </g>

  <g class="front-wall">
    <path class="panel" d="M557 742 L1127 742 L1127 755 L1255 755 Q1265 755 1265 765 L1265 875 Q1265 885 1255 885 L1127 885 L1127 895 L557 895 L557 885 L424 885 Q414 885 414 875 L414 765 Q414 755 424 755 L557 755 Z"/>
    <g clip-path="url(#front-clip)">
      <rect class="band" x="405" y="788" width="870" height="64"/>
      <line class="band-stitch" x1="405" y1="800" x2="1275" y2="800"/>
      <line class="band-stitch" x1="405" y1="840" x2="1275" y2="840"/>
    </g>
    <line class="fold" x1="557" y1="755" x2="557" y2="885"/>
    <line class="fold" x1="1127" y1="755" x2="1127" y2="885"/>
    <line class="fold" x1="557" y1="895" x2="1127" y2="895"/>
    <circle class="name-disc" cx="847" cy="820" r="49"/>
    <text class="brand-name" x="847" y="827" text-anchor="middle">Tovarin</text>
  </g>

  <g class="base">
    <path class="panel" d="M233 903 L378 897 L378 1273 L233 1267 L233 1140 L218 1135 L218 1032 L233 1026 Z"/>
    <path class="panel" d="M1445 903 L1300 897 L1300 1273 L1445 1267 L1445 1140 L1460 1135 L1460 1032 L1445 1026 Z"/>
    <rect class="panel" x="378" y="897" width="172" height="376"/>
    <rect class="panel" x="1127" y="897" width="173" height="376"/>
    <rect class="panel" x="550" y="895" width="577" height="378"/>

    <rect class="band" x="445" y="897" width="62" height="376"/>
    <rect class="info-panel" x="428" y="968" width="92" height="232"/>
    <g transform="translate(474 1084) rotate(-90)">
      <text class="info-text" x="0" y="-18" text-anchor="middle">This is English text and there will not be much</text>
      <text class="info-text" x="0" y="4" text-anchor="middle">more than these characters, but also there will be</text>
      <text class="info-text" x="0" y="26" text-anchor="middle">German translation in this same space</text>
    </g>

    <rect class="band" x="1172" y="897" width="64" height="376"/>
    <rect class="info-panel" x="1158" y="968" width="92" height="232"/>
    <g transform="translate(1204 1084) rotate(90)">
      <text class="info-text" x="0" y="-18" text-anchor="middle">This is English text and there will not be much</text>
      <text class="info-text" x="0" y="4" text-anchor="middle">more than these characters, but also there will be</text>
      <text class="info-text" x="0" y="26" text-anchor="middle">German translation in this same space</text>
    </g>

    <line class="fold" x1="378" y1="897" x2="378" y2="1273"/>
    <line class="fold" x1="398" y1="897" x2="398" y2="1273"/>
    <line class="fold" x1="550" y1="897" x2="550" y2="1273"/>
    <line class="fold" x1="1127" y1="897" x2="1127" y2="1273"/>
    <line class="fold" x1="1280" y1="897" x2="1280" y2="1273"/>
    <line class="fold" x1="1300" y1="897" x2="1300" y2="1273"/>
    <line class="fold" x1="550" y1="1273" x2="1127" y2="1273"/>

    <rect class="slot" x="547" y="1028" width="19" height="114"/>
    <rect class="slot" x="1112" y="1028" width="19" height="114"/>
  </g>

  <g class="back-wall">
    <path class="panel" d="M566 1273 L1113 1273 L1113 1285 L1255 1285 Q1265 1285 1265 1295 L1265 1405 Q1265 1415 1255 1415 L1113 1415 L1113 1425 L566 1425 L566 1415 L424 1415 Q414 1415 414 1405 L414 1295 Q414 1285 424 1285 L566 1285 Z"/>
    <line class="fold" x1="566" y1="1285" x2="566" y2="1415"/>
    <line class="fold" x1="1113" y1="1285" x2="1113" y2="1415"/>
    <circle class="name-disc" cx="840" cy="1350" r="49"/>
    <text class="brand-name" x="840" y="1357" text-anchor="middle" transform="rotate(180 840 1350)">Tovarin</text>
  </g>
</svg>
</body>
</html>
```